Velvet Crypt Mixtape Podcast Design

My audio drama podcast is a funny horror story with romantic elements called Velvet Crypt Mixtape.
I'm looking for a colorful design featuring the title and letting the viewer know this is a horror show.
The title needs to be clearly visible even in thumbnail size.

```html
<!DOCTYPE html>
<html lang="en">
<head>
<meta charset="utf-8">
<title>Velvet Crypt Mixtape – Podcast Cover</title>
<link rel="stylesheet" href="https://fonts.googleapis.com/css2?family=Anton&display=swap">
<style>
  :root {
    --stage: #1c2640;
    --cover-violet: #43448f;
    --cover-violet-deep: #34356f;
    --cover-violet-light: #5658a8;
    --frame-green: #23c486;
    --band-green: #12c684;
    --band-orange: #f68a0f;
    --title-violet: #4b4ca6;
    --title-shadow: #25264f;
    --ring: rgba(220, 225, 255, 0.22);
  }
  * { margin: 0; padding: 0; box-sizing: border-box; }
  html, body {
    width: 1200px;
    height: 807px;
    overflow: hidden;
    background: var(--stage);
  }
  .stage {
    position: relative;
    width: 1200px;
    height: 807px;
  }
  .cover {
    position: absolute;
    left: 250px;
    top: 53px;
    width: 700px;
    height: 700px;
    overflow: hidden;
    background: var(--cover-violet);
  }
  .cover-texture {
    position: absolute;
    inset: 0;
    background:
      radial-gradient(ellipse at 35% 15%, var(--cover-violet-light) 0%, transparent 55%),
      radial-gradient(ellipse at 80% 90%, var(--cover-violet-deep) 0%, transparent 60%),
      linear-gradient(160deg, var(--cover-violet) 0%, var(--cover-violet-deep) 100%);
  }
  .cover-art {
    position: absolute;
    inset: 0;
  }
  .cover-title {
    position: absolute;
    left: 350px;
    top: 368px;
    transform: translate(-50%, -50%) rotate(-16.7deg);
    font-family: "Anton", Impact, sans-serif;
    color: var(--title-violet);
    text-transform: uppercase;
    line-height: 0.92;
    text-align: left;
    white-space: nowrap;
    text-shadow: -4px 5px 0 var(--title-shadow);
  }
  .cover-title .line-top {
    display: block;
    font-size: 74px;
    letter-spacing: 1px;
  }
  .cover-title .line-bottom {
    display: block;
    font-size: 112px;
    letter-spacing: 2px;
  }
</style>
</head>
<body>
  <main class="stage">
    <section class="cover" aria-label="Velvet Crypt Mixtape podcast cover">
      <div class="cover-texture" role="img" aria-label="Misty night forest texture in deep violet tones"></div>
      <svg class="cover-art" width="700" height="700" viewBox="0 0 700 700" aria-hidden="true">
        <circle cx="350" cy="360" r="300" fill="none" stroke="var(--ring)" stroke-width="3"/>
        <rect x="35" y="35" width="630" height="630" fill="none" stroke="var(--frame-green)" stroke-width="1.5"/>
        <polygon points="0,345 700,135 700,390 0,600" fill="var(--band-green)"/>
        <polygon points="0,380 700,170 700,355 0,565" fill="var(--band-orange)"/>
      </svg>
      <h1 class="cover-title">
        <span class="line-top">Velvet Crypt</span>
        <span class="line-bottom">Mixtape</span>
      </h1>
    </section>
  </main>
</body>
</html>
```